Corporate Website - KWARTA HOLDINGS, LLC

This Nevada Corporation has several subsidiaries:
T. M. Designs - Interior Design; Commercial, Residential & Hospitality
T. M. Style - Fashion Design & Styling
FERN LOUNGE - Upscale Membership Only Lounge servicing Business Men and women. It is located in Accra, Ghana
FERN SUITES - Full Service Executive Suites for top Businesses. Located in Accra, Ghana.
THE MATERIAL YARD - Distributor for Building and Interior Design Materials
URL: www.kwartaholdingsllc.example
Website: info@kwartaholdingsllc.example
Phones: 1 702-555-0147 Las Vegas; +233 26 5550193 Ghana

Industry/Entity Type

Fashion

```html
<!DOCTYPE html>
<html lang="en">
<head>
<meta charset="utf-8">
<title>Kwarta Holdings, LLC</title>
<link href="https://fonts.googleapis.com/css2?family=Advent+Pro:wght@300;400;600&family=Yanone+Kaffeesatz:wght@400;600&family=Lato:wght@300;400;700&display=swap" rel="stylesheet">
<style>
  :root {
    --topbar: #0c0506;
    --header: #0b0b0b;
    --accent: #2aa7d3;
    --footer: #2c3437;
    --footer-deep: #1b2123;
    --ink: #1a1a1a;
    --ink-soft: #4a4a4a;
    --white: #ffffff;
    --steel: #4d82a8;
    --cond: "Yanone Kaffeesatz", "Arial Narrow", sans-serif;
    --thin: "Advent Pro", "Helvetica Neue", sans-serif;
    --body: "Lato", Arial, sans-serif;
  }
  * { margin: 0; padding: 0; box-sizing: border-box; }
  html, body { width: 1045px; height: 1200px; overflow: hidden; }
  body { position: relative; background: var(--white); font-family: var(--body); }
  .abs { position: absolute; }

  .topbar { left: 0; top: 0; width: 1045px; height: 27px; background: var(--topbar); color: var(--white); font-family: var(--cond); font-size: 11px; }
  .topbar .contacts { left: 79px; top: 6px; display: flex; gap: 8px; white-space: nowrap; }
  .topbar .contacts span { display: inline-flex; align-items: center; gap: 4px; }
  .social-dots { display: flex; gap: 17px; }
  .topbar .social-dots { left: 870px; top: 7px; }
  .dot { width: 11px; height: 11px; border-radius: 50%; background: var(--white); display: inline-block; }

  .site-header { left: 0; top: 27px; width: 1045px; height: 96px; background: var(--header); }
  .brand { left: 76px; top: 34px; color: var(--white); font-family: var(--cond); font-size: 21px; font-weight: 600; letter-spacing: .3px; }
  .nav { top: 41px; display: flex; font-family: var(--cond); font-size: 11px; color: var(--accent); text-transform: uppercase; }
  .nav a { position: absolute; color: inherit; text-decoration: none; white-space: nowrap; display: inline-flex; gap: 5px; align-items: center; }

  .hero { left: 0; top: 123px; width: 1045px; height: 345px;
    background: linear-gradient(180deg, #5a4a3c 0%, #8a7560 35%, #6a4c36 70%, #3a2a20 100%); }
  .hero-card { left: 76px; top: 252px; width: 279px; height: 167px; background: rgba(228,226,224,.88); padding: 22px 0 0 23px; }
  .hero-card h1 { font-family: var(--cond); font-weight: 600; font-size: 29px; color: var(--ink); letter-spacing: .8px; line-height: 30px; white-space: nowrap; }
  .hero-card h1 .dash { font-family: var(--thin); font-weight: 300; }
  .hero-card p { font-family: var(--thin); font-weight: 400; font-size: 27px; line-height: 30px; color: var(--ink); }

  .tagline { left: 78px; top: 520px; width: 660px; font-family: var(--thin); font-weight: 400; font-size: 27px; line-height: 31px; color: var(--ink-soft); }
  .tagline strong { font-weight: 600; color: #333; }
  .btn { display: flex; align-items: center; justify-content: center; gap: 10px; color: var(--white); font-family: var(--cond); }
  .btn-dark { left: 759px; top: 525px; width: 178px; height: 40px; background: #000; font-size: 21px; }
  .btn-steel { left: 828px; top: 807px; width: 134px; height: 41px; background: var(--steel); border: 1px solid var(--white); font-size: 13px; }

  .suites-photo { left: 0; top: 620px; width: 1045px; height: 302px;
    background: linear-gradient(90deg, #9a9392 0%, #5e3c30 45%, #7a6a62 75%, #6a6868 100%); }
  .suites-band { left: 0; top: 670px; width: 1045px; height: 220px; background: rgba(236,236,236,.88); }
  .suites-name { left: 150px; top: 812px; width: 134px; text-align: center; font-family: var(--cond); font-size: 24px; color: var(--ink); }
  .suites-text { left: 380px; top: 737px; width: 600px; font-family: var(--body); font-weight: 300; font-size: 21px; line-height: 26px; color: var(--ink); }

  .site-footer { left: 0; top: 922px; width: 1045px; height: 221px; background: var(--footer); color: var(--white); }
  .footer-brand { left: 77px; top: 940px; font-family: var(--cond); font-size: 23px; font-weight: 600; color: var(--white); }
  .footer-about { left: 77px; top: 983px; width: 422px; font-family: var(--cond); font-size: 10.4px; line-height: 14.6px; color: var(--white); }
  .footer-mail { left: 77px; top: 1056px; width: 420px; height: 31px; border: 1px solid var(--white); display: flex; align-items: center; justify-content: center; gap: 6px; font-family: var(--body); font-size: 10px; color: var(--white); }
  .footer-phones { left: 81px; top: 1094px; font-family: var(--cond); font-size: 15px; line-height: 16px; color: var(--white); }
  .footer-phones div { display: flex; align-items: center; gap: 3px; }
  .stay { left: 762px; top: 966px; width: 189px; padding-bottom: 3px; border-bottom: 1px solid var(--white); font-family: var(--thin); font-size: 16px; color: var(--white); }
  .social-tiles { left: 759px; top: 1000px; display: flex; }
  .social-tiles span { width: 28px; height: 27px; background: #000; display: flex; align-items: center; justify-content: center; border-top: 2px solid; }
  .social-tiles .dot { width: 8px; height: 8px; }
  .to-top { left: 964px; top: 1107px; width: 39px; height: 36px; background: #2a2f31; border: 1px solid #3a4144; display: flex; align-items: center; justify-content: center; }
  .footer-bar { left: 0; top: 1143px; width: 1045px; height: 57px; background: var(--footer-deep); }
  .copyright { left: 77px; top: 1170px; font-family: var(--body); font-size: 8px; color: var(--white); }
  .up-arrow { left: 954px; top: 1169px; }
</style>
</head>
<body>
  <div class="abs topbar">
    <div class="abs contacts">
      <span><svg width="8" height="8" viewBox="0 0 10 10"><path d="M2 0l2 2-1 1.5a6 6 0 003.5 3.5L8 6l2 2-1.5 2C4 10 0 6 0 1.5z" fill="#fff"/></svg>+1 (702) 555-0147 ( LAS VEGAS )</span>
      <span>|</span>
      <span><svg width="8" height="8" viewBox="0 0 10 10"><path d="M2 0l2 2-1 1.5a6 6 0 003.5 3.5L8 6l2 2-1.5 2C4 10 0 6 0 1.5z" fill="#fff"/></svg>+233 26 5550193 ( GHANA )</span>
      <span>|</span>
      <span><svg width="9" height="7" viewBox="0 0 10 8"><rect width="10" height="8" fill="#fff"/><path d="M0 0l5 4 5-4" stroke="#0c0506" fill="none"/></svg>info@KwartaHoldingsLLC.example</span>
    </div>
    <div class="abs social-dots"><span class="dot"></span><span class="dot"></span><span class="dot"></span><span class="dot"></span></div>
  </div>

  <header class="abs site-header">
    <div class="abs brand">KWARTA HOLDINGS, LLC</div>
    <nav class="abs nav" style="left:0;width:1045px;">
      <a style="left:755px">Services</a>
      <a style="left:810px">About us</a>
      <a style="left:857px">Page 1</a>
      <a style="left:916px"><svg width="10" height="8" viewBox="0 0 10 8"><rect x=".5" y=".5" width="9" height="7" fill="none" stroke="#2aa7d3"/><path d="M.5 .5l4.5 4 4.5-4" stroke="#2aa7d3" fill="none"/></svg>Contact</a>
    </nav>
  </header>

  <div class="abs hero" role="img" aria-label="Photo of a modern restaurant interior with dark pillars, red wall panels and set tables"></div>
  <div class="abs hero-card">
    <h1>THE MATERIAL YARD <span class="dash">-</span></h1>
    <p>Distributor for<br>Building and Interior<br>Design Materials</p>
  </div>

  <p class="abs tagline">Your <strong>Trusted</strong> Resource for Commercial Building and Interior Design Materials</p>
  <div class="abs btn btn-dark">Send an enquiry
    <svg width="26" height="26" viewBox="0 0 26 26"><circle cx="13" cy="13" r="11.5" fill="none" stroke="#fff" stroke-width="2"/><path d="M7 13h11M14 9l4 4-4 4" stroke="#fff" stroke-width="2" fill="none"/></svg>
  </div>

  <div class="abs suites-photo" role="img" aria-label="Photo of an office lobby with wood panelling and two businesswomen reviewing papers"></div>
  <div class="abs suites-band"></div>
  <svg class="abs" style="left:178px;top:720px" width="79" height="79" viewBox="0 0 79 79">
    <circle cx="39.5" cy="39.5" r="36" fill="none" stroke="#2aa7d3" stroke-width="5"/>
    <circle cx="37" cy="29" r="9" fill="#2aa7d3"/>
    <path d="M21 56c0-10 7-16 16-16s16 6 16 16z" fill="#2aa7d3"/>
    <path d="M55 22v9M50.5 26.5h9" stroke="#2aa7d3" stroke-width="2.5"/>
  </svg>
  <div class="abs suites-name">FERN SUITES</div>
  <p class="abs suites-text">Full Service Executive Suites for top Businesses. Located in Accra, Ghana.</p>
  <div class="abs btn btn-steel">Send an enquiry
    <svg width="24" height="24" viewBox="0 0 26 26"><circle cx="13" cy="13" r="11.5" fill="none" stroke="#fff" stroke-width="2"/><path d="M7 13h11M14 9l4 4-4 4" stroke="#fff" stroke-width="2" fill="none"/></svg>
  </div>

  <footer class="abs site-footer"></footer>
  <div class="abs footer-brand">KWARTA HOLDINGS, LLC</div>
  <p class="abs footer-about">Lorem ipsum is demo text is to preview. Here goes some information about company,. a short description. Lorem ipsum is demo text is to preview. Here goes some information about company,. a short description. Lorem ipsum is demo text is to preview. Here goes some information about company,. a short description. Lorem ipsum is demo text is to preview. Here goes some information about company,. a short description.</p>
  <div class="abs footer-mail"><svg width="10" height="10" viewBox="0 0 10 10"><path d="M10 0L0 4l3.5 1.5L10 0 4.5 6.5V10l2-2.5L9 9z" fill="none" stroke="#fff" stroke-width=".9"/></svg>info@KwartaHoldingsLLC.example</div>
  <div class="abs footer-phones">
    <div><svg width="11" height="11" viewBox="0 0 10 10"><path d="M2 0l2 2-1 1.5a6 6 0 003.5 3.5L8 6l2 2-1.5 2C4 10 0 6 0 1.5z" fill="#fff"/></svg>+1 (702) 555-0147 ( Las Vegas )</div>
    <div><svg width="11" height="11" viewBox="0 0 10 10"><path d="M2 0l2 2-1 1.5a6 6 0 003.5 3.5L8 6l2 2-1.5 2C4 10 0 6 0 1.5z" fill="#fff"/></svg>+233 26 5550193 ( Ghana )</div>
  </div>
  <div class="abs stay">Stay in touch</div>
  <div class="abs social-tiles">
    <span style="border-color:#3b5b99"><i class="dot"></i></span>
    <span style="border-color:#c0392b"><i class="dot"></i></span>
    <span style="border-color:#2aa7d3"><svg width="10" height="8" viewBox="0 0 10 8"><rect x=".5" y=".5" width="9" height="7" fill="none" stroke="#fff"/><path d="M.5 .5l4.5 4 4.5-4" stroke="#fff" fill="none"/></svg></span>
    <span style="border-color:#1d6fa5"><i class="dot"></i></span>
  </div>
  <div class="abs to-top"><svg width="9" height="6" viewBox="0 0 9 6"><path d="M1 5l3.5-3.5L8 5" stroke="#8a9396" fill="none"/></svg></div>

  <div class="abs footer-bar"></div>
  <div class="abs copyright">© 2015 Kwarta Holdings, LLC | All Rights Reserved | Developed by Rohan ( mail@rohan.example )</div>
  <svg class="abs up-arrow" width="9" height="10" viewBox="0 0 9 10"><path d="M4.5 1v9M1 4.5l3.5-3.5L8 4.5" stroke="#fff" stroke-width="2" fill="none"/></svg>
</body>
</html>
```